Create Template Proposal Coversheet

We need a proposal Cover Sheet & Page Template for residential architectural projects. For the Cover Sheet, we want a variety of images blends and set as a background image for the title of the proposal for prospective clients. We need it in a format that we can type over the top of the image (maybe whited-out in the middle) so we can use it for all our proposals. Our logo should be clear and sharp in a corner (but we will leave that up to the designer. Not all images need to be used. For the Page Template we want a consistent look on the page with our logo, company address & contact information and a design element that ties the entire proposal together. Our proposals consist of a Cover page, Project information sheet, a picture of the property, the proposal for services (3-5 pages), Expect fees page and a timeline page.

Target Market(s)

Homeowners, 35 - 60 years old

Industry/Entity Type

Architecture

Font styles to use
Serif

Colors
3176b5
f68d4c
ec1f27
fbee3f

Requirements
Must have
• The cover should have a nice blend of images - looking for something that shows the whole design process - from initial sketches to working drawings, construction and finished home. These images are background to the title of the proposal

```html
<!DOCTYPE html>
<html lang="en">
<head>
<meta charset="utf-8">
<title>Harlow Reed Architect — Proposal Template</title>
<link href="https://fonts.googleapis.com/css2?family=Cinzel:wght@400;500&family=Crimson+Text:wght@400;600&display=swap" rel="stylesheet">
<style>
  :root{
    --navy:#2c2a7c;
    --blue:#2e3192;
    --orange:#f37b20;
    --yellow:#f7ec3f;
    --red:#e31e26;
    --ink:#2a2a2a;
    --board:#ebebeb;
    --white:#ffffff;
    --grey-1:#9a9a9a;
    --grey-2:#222222;
    --grey-3:#777777;
    --grey-4:#444444;
  }
  *{margin:0;padding:0;box-sizing:border-box}
  html,body{width:1200px;height:1021px;overflow:hidden;background:var(--board)}
  body{font-family:"Crimson Text",Georgia,serif;color:var(--ink)}
  .board{position:absolute;left:0;top:0;width:2074px;height:1764px;transform:scale(0.578592);transform-origin:0 0}
  .page{position:absolute;width:617px;height:800px;background:var(--white);overflow:hidden}
  .abs{position:absolute}
  .heading{font-family:"Cinzel",Georgia,serif;font-weight:400;font-size:23px;line-height:30px;letter-spacing:.3px}
  .small-label{font-size:11px;letter-spacing:1px;text-transform:uppercase}
  .photo{position:absolute}
  .timeline-line{position:absolute;width:2px}
  .node{position:absolute;width:24px;height:24px;border-radius:50%;background:var(--white);border:2px solid}
  .connector{position:absolute;height:1.5px}
  .step{position:absolute;width:165px;text-align:center;font-size:11px;line-height:13px;color:var(--ink)}
  .step b{display:block;font-weight:400;font-size:11.5px;letter-spacing:.3px}
  .icon{position:absolute;width:46px;height:46px;fill:none;stroke:currentColor;stroke-width:2.6;stroke-linecap:round;stroke-linejoin:round}
  .body-copy{font-size:11.5px;line-height:14.6px;text-align:justify}
  .brand-name{font-family:"Crimson Text",Georgia,serif;font-weight:600;color:var(--navy);text-align:center;text-transform:uppercase}

  /* cover */
  .cover .panel{left:308px;top:0;width:309px;height:800px;background:var(--navy)}
  .cover .sun{width:124px;height:124px;border-radius:50%;background:var(--yellow)}
  .cover .frame{left:32px;top:257px;width:276px;height:317px;background:var(--navy)}
  .cover .frame-inner{left:51px;top:275px;width:257px;height:282px;background:var(--white)}
  .cover .footer{left:13px;top:771px;font-size:11px;letter-spacing:3px;font-variant:small-caps;text-transform:none}

  /* services */
  .services-navy .panel{left:0;top:0;width:216px;height:394px;background:var(--navy)}
  .services-orange .panel{left:404px;top:0;width:213px;height:391px;background:var(--orange)}

  /* timeframe */
  .bar{position:absolute;height:21px}
  .bar-label{position:absolute;font-size:11px;line-height:13px;text-align:center;transform:translateX(-50%);white-space:nowrap}
  .bar-text{color:var(--white);font-size:10px;letter-spacing:3.5px;text-align:center;line-height:20px;font-weight:600}
  .dash{position:absolute;width:0;border-left:1.5px dashed var(--blue)}

  /* prices */
  .price-table{position:absolute;left:20px;top:80px;border-collapse:collapse;font-size:11px}
  .price-table td,.price-table th{border:1px solid #555;text-align:center;padding:0}
  .price-table th{background:var(--orange);color:var(--white);font-weight:400;letter-spacing:1px;height:16px;font-size:9.5px}
  .price-table .row-label{border:none;text-align:right;padding-right:6px;width:83px}
  .price-table .baths td{height:20px}
  .price-table .story td{height:39px}
  .spread{display:flex;justify-content:space-around}
  .price-list{position:absolute;left:23px;top:287px;color:var(--navy);font-size:13px;line-height:17px}
  .price-row{display:flex}
  .price-row .lbl{width:118px}
  .price-row .cur{width:12px}
  .price-row .amt{width:66px;text-align:right}
  .accent{color:var(--blue)}
  .contact{color:var(--white);text-align:center;font-size:11.5px;line-height:17px;letter-spacing:.5px}
</style>
</head>
<body>
<main class="board">

  <!-- Cover -->
  <section class="page cover" style="left:66px;top:58px">
    <div class="abs panel"></div>
    <div class="abs brand-name" style="left:20px;top:112px;width:262px;font-size:27px;line-height:30px;letter-spacing:.5px">Harlow Reed<br>Architect</div>
    <h1 class="abs heading" style="left:326px;top:24px;color:var(--white);font-size:24px">A Home Like NO Other</h1>
    <p class="abs body-copy" style="left:327px;top:72px;width:270px;color:var(--white)">Lorem ipsum dolor sit amet, consectetuer adipiscing elit, sed diam nonummy nibh euismod tincidunt ut laoreet dolore magna aliquam erat volutpat. Ut wisi enim ad minim veniam, quis nostrud exerci tation ullamcorper suscipit lobortis nisl ut aliquip ex ea commodo consequat. Duis autem vel eum iriure dolor in hendrerit in vulputate velit esse molestie consequat, vel illum dolore eu feugiat nulla facilisis at vero eros et accumsan et iusto odio dignissim qui blandit praesent luptatum zzril delenit.</p>
    <div class="abs sun" style="left:22px;top:220px"></div>
    <div class="abs sun" style="left:182px;top:520px"></div>
    <div class="abs frame"></div>
    <div class="abs frame-inner"></div>
    <div class="photo" role="img" aria-label="Photograph of a finished timber-frame home with stone walls and gardens" style="left:79px;top:314px;width:458px;height:280px;background:linear-gradient(170deg,#7f9a78 0%,#8d6a4f 45%,#a0563f 65%,#5f7a45 100%)"></div>
    <div class="abs footer">Lorem Ipsum -2020</div>
  </section>

  <!-- Services (navy) -->
  <section class="page services-navy" style="left:729px;top:58px">
    <div class="abs panel"></div>
    <h2 class="abs heading" style="left:20px;top:24px;width:169px;text-align:right;color:var(--white)">Lorem Ipsum<br>Dolor Sit<br>Services</h2>
    <svg class="abs" style="left:0;top:0" width="216" height="394"><path d="M0 197 A202 202 0 0 1 157 394" fill="none" stroke="#fff" stroke-width="5"/></svg>
    <div class="photo" role="img" aria-label="Rolled architectural blueprints and working drawings" style="left:0;top:394px;width:216px;height:406px;background:linear-gradient(160deg,#dfe8f6 0%,#b7c9e8 50%,#8ea9d8 100%)"></div>

    <div class="timeline-line" style="left:506px;top:32px;height:736px;background:var(--blue)"></div>

    <div class="connector" style="left:455px;top:59px;width:40px;background:var(--blue)"></div>
    <div class="node" style="left:495px;top:47px;border-color:var(--blue)"></div>
    <div class="step" style="left:290px;top:38px"><b>LOREM IPSUM</b>Lorem ipsum dolor sit amet, consec-<br>tetuer adipiscing elit,</div>

    <div class="connector" style="left:401px;top:156px;width:94px;background:var(--blue)"></div>
    <div class="node" style="left:495px;top:144px;border-color:var(--blue)"></div>
    <div class="step" style="left:236px;top:135px"><b>LOREM IPSUM</b>Lorem ipsum dolor sit amet, consec-<br>tetuer adipiscing elit,</div>

    <div class="connector" style="left:455px;top:253px;width:40px;background:var(--blue)"></div>
    <div class="node" style="left:495px;top:241px;border-color:var(--blue)"></div>
    <div class="step" style="left:290px;top:232px"><b>LOREM IPSUM</b>Lorem ipsum dolor sit amet, consec-<br>tetuer adipiscing elit,</div>

    <div class="connector" style="left:401px;top:350px;width:94px;background:var(--blue)"></div>
    <div class="node" style="left:495px;top:338px;border-color:var(--blue)"></div>
    <div class="step" style="left:236px;top:329px"><b>LOREM IPSUM</b>Lorem ipsum dolor sit amet, consec-<br>tetuer adipiscing elit,</div>

    <div class="connector" style="left:455px;top:447px;width:40px;background:var(--blue)"></div>
    <div class="node" style="left:495px;top:435px;border-color:var(--blue)"></div>
    <div class="step" style="left:290px;top:426px"><b>LOREM IPSUM</b>Lorem ipsum dolor sit amet, consec-<br>tetuer adipiscing elit,</div>

    <div class="connector" style="left:401px;top:544px;width:94px;background:var(--blue)"></div>
    <div class="node" style="left:495px;top:532px;border-color:var(--blue)"></div>
    <div class="step" style="left:236px;top:523px"><b>LOREM IPSUM</b>Lorem ipsum dolor sit amet, consec-<br>tetuer adipiscing elit,</div>

    <div class="connector" style="left:455px;top:641px;width:40px;background:var(--blue)"></div>
    <div class="node" style="left:495px;top:629px;border-color:var(--blue)"></div>
    <div class="step" style="left:290px;top:620px"><b>LOREM IPSUM</b>Lorem ipsum dolor sit amet, consec-<br>tetuer adipiscing elit,</div>

    <div class="connector" style="left:401px;top:739px;width:94px;background:var(--blue)"></div>
    <div class="node" style="left:495px;top:727px;border-color:var(--blue)"></div>
    <div class="step" style="left:236px;top:718px"><b>LOREM IPSUM</b>Lorem ipsum dolor sit amet, consec-<br>tetuer adipiscing elit,</div>

    <svg class="icon" viewBox="0 0 48 48" style="left:544px;top:36px;color:var(--blue)"><path d="M24 4v6"/><circle cx="24" cy="14" r="4"/><path d="M21 17L10 43M27 17l11 26M14 33h20"/></svg>
    <svg class="icon" viewBox="0 0 48 48" style="left:544px;top:133px;color:var(--blue)"><rect x="7" y="7" width="34" height="34"/><rect x="4" y="4" width="6" height="6"/><rect x="38" y="4" width="6" height="6"/><rect x="4" y="38" width="6" height="6"/><rect x="38" y="38" width="6" height="6"/><path d="M15 15h18M24 15v18M20 33h8"/></svg>
    <svg class="icon" viewBox="0 0 48 48" style="left:544px;top:230px;color:var(--blue)"><path d="M6 4v38h38"/><rect x="12" y="26" width="10" height="16"/><rect x="22" y="32" width="16" height="10"/><path d="M12 20L24 8l6 6-12 12"/></svg>
    <svg class="icon" viewBox="0 0 48 48" style="left:544px;top:327px;color:var(--blue)"><path d="M14 4v30h30M4 14h30v30M14 34l20-20"/><rect x="18" y="18" width="12" height="12"/></svg>
    <svg class="icon" viewBox="0 0 48 48" style="left:544px;top:424px;color:var(--blue)"><circle cx="24" cy="15" r="11"/><path d="M28 10h-5a3 3 0 0 0 0 6h3a3 3 0 0 1 0 6h-5M24 7v16M24 26v18M24 40c-8 0-11-5-12-9 7 0 11 4 12 9 1-5 5-9 12-9-1 4-4 9-12 9"/></svg>
    <svg class="icon" viewBox="0 0 48 48" style="left:544px;top:521px;color:var(--blue)"><rect x="5" y="5" width="38" height="38"/><path d="M24 5v10a3 3 0 0 1 0 6v22M5 24h10a3 3 0 0 0 6 0h22"/></svg>
    <svg class="icon" viewBox="0 0 48 48" style="left:544px;top:618px;color:var(--blue)"><circle cx="24" cy="8" r="4"/><path d="M17 20a7 7 0 0 1 14 0"/><circle cx="11" cy="31" r="4"/><circle cx="37" cy="31" r="4"/><path d="M4 44a7 7 0 0 1 14 0M30 44a7 7 0 0 1 14 0M24 20v6M14 26h20"/></svg>
    <svg class="icon" viewBox="0 0 48 48" style="left:544px;top:716px;color:var(--blue)"><circle cx="24" cy="24" r="16"/><circle cx="24" cy="24" r="6"/><path d="M24 2v10M24 36v10M2 24h10M36 24h10"/></svg>
  </section>

  <!-- Time frame -->
  <section class="page timeframe" style="left:1391px;top:58px">
    <div class="photo" role="img" aria-label="Photograph of a timber entrance pavilion with stone piers" style="left:120px;top:0;width:242px;height:329px;background:linear-gradient(180deg,#b9cbe0 0%,#a55a36 40%,#8c4a2e 65%,#9a948a 100%)"></div>
    <div class="photo" role="img" aria-label="Photograph of a timber-frame home entrance among trees" style="left:374px;top:0;width:243px;height:329px;background:linear-gradient(180deg,#c7d8ec 0%,#5f7d4a 35%,#a4583a 60%,#b7b1a6 100%)"></div>
    <div class="abs" style="left:128px;top:8px;width:232px;height:313px;border-left:3px solid #fff;border-bottom:3px solid #fff;border-top:3px solid #fff;border-right:3px solid #fff;clip-path:polygon(0 0,100% 0,100% 8%,8% 8%,8% 100%,0 100%)"></div>
    <div class="abs" style="left:382px;top:8px;width:226px;height:313px;border:3px solid #fff;clip-path:polygon(0 0,100% 0,100% 100%,0 100%,0 92%,92% 92%,92% 0)"></div>

    <h2 class="abs heading" style="left:34px;top:356px;color:var(--navy)">Time Frame and Instalments</h2>
    <div class="abs small-label" style="left:34px;top:410px">Traditional Constructions</div>

    <div class="bar-label" style="left:84px;top:438px">Site Analysis<br>&amp; Design</div>
    <div class="bar-label" style="left:175px;top:452px">Permits</div>
    <div class="bar-label" style="left:253px;top:437px">Site<br>Preparation</div>
    <div class="bar-label" style="left:449px;top:452px">Construction</div>
    <div class="bar" style="left:34px;top:469px;width:102px;background:var(--grey-1)"></div>
    <div class="bar" style="left:142px;top:469px;width:65px;background:var(--grey-2)"></div>
    <div class="bar" style="left:215px;top:469px;width:79px;background:var(--grey-3)"></div>
    <div class="bar" style="left:300px;top:469px;width:282px;background:var(--grey-4)"></div>

    <div class="abs small-label" style="left:34px;top:534px">Harlow Reed Architect&nbsp; Constructions</div>
    <div class="bar-label" style="left:84px;top:565px">Site Analysis<br>&amp; Design</div>
    <div class="bar-label" style="left:286px;top:576px">Manufacturing Lorem ipsum</div>
    <div class="bar-label" style="left:508px;top:585px">Time Saved</div>
    <div class="bar bar-text" style="left:34px;top:596px;width:102px;background:var(--navy)">5 WEEKS</div>
    <div class="bar bar-text" style="left:140px;top:596px;width:281px;background:var(--orange)">6 MONTHS</div>
    <svg class="abs" style="left:425px;top:594px" width="160" height="26"><path d="M2 2v22M2 12h155M157 2v22" stroke="var(--red)" stroke-width="2" fill="none"/></svg>

    <div class="dash" style="left:136px;top:620px;height:115px"></div>
    <div class="dash" style="left:336px;top:620px;height:86px"></div>
    <div class="dash" style="left:379px;top:620px;height:104px"></div>
    <div class="dash" style="left:422px;top:620px;height:104px"></div>
    <div class="dash" style="left:466px;top:620px;height:58px"></div>

    <div class="bar-label" style="left:174px;top:648px">Permits</div>
    <div class="bar" style="left:142px;top:664px;width:64px;background:var(--yellow)"></div>
    <div class="bar-label" style="left:292px;top:633px">Site<br>Preparation</div>
    <div class="bar" style="left:254px;top:664px;width:78px;background:var(--blue)"></div>

    <div class="abs" style="left:34px;top:734px;font-size:11px;line-height:13px">Value<br>150K</div>
    <div class="bar-label" style="left:135px;top:734px">Agreement<br>30%</div>
    <div class="bar-label" style="left:314px;top:707px">Installation<br>30%</div>
    <div class="bar-label" style="left:379px;top:725px">Finishes<br>30%</div>
    <div class="bar-label" style="left:442px;top:725px">Hand Over<br>5%</div>
    <div class="bar-label" style="left:496px;top:679px">Lorem ipsum<br>5%</div>
  </section>

  <!-- Services (orange) -->
  <section class="page services-orange" style="left:66px;top:901px">
    <div class="abs panel"></div>
    <h2 class="abs heading" style="left:432px;top:20px;color:var(--white)">Lorem Ipsum<br>&nbsp;Dolor Sit<br>Services</h2>
    <svg class="abs" style="left:404px;top:0" width="213" height="391"><path d="M212 194 A202 202 0 0 0 63 389" fill="none" stroke="#fff" stroke-width="5"/></svg>
    <div class="photo" role="img" aria-label="Rolled architectural drawings in warm sepia tones" style="left:404px;top:391px;width:213px;height:409px;background:linear-gradient(160deg,#f5c9a6 0%,#e9b892 55%,#d6a788 100%)"></div>

    <div class="timeline-line" style="left:113px;top:27px;height:738px;background:var(--orange)"></div>

    <div class="connector" style="left:126px;top:54px;width:41px;background:var(--orange)"></div>
    <div class="node" style="left:102px;top:42px;border-color:var(--orange)"></div>
    <div class="step" style="left:167px;top:33px"><b>LOREM IPSUM</b>Lorem ipsum dolor sit amet, consec-<br>tetuer adipiscing elit,</div>

    <div class="connector" style="left:126px;top:152px;width:94px;background:var(--orange)"></div>
    <div class="node" style="left:102px;top:140px;border-color:var(--orange)"></div>
    <div class="step" style="left:220px;top:131px"><b>LOREM IPSUM</b>Lorem ipsum dolor sit amet, consec-<br>tetuer adipiscing elit,</div>

    <div class="connector" style="left:126px;top:249px;width:41px;background:var(--orange)"></div>
    <div class="node" style="left:102px;top:237px;border-color:var(--orange)"></div>
    <div class="step" style="left:167px;top:228px"><b>LOREM IPSUM</b>Lorem ipsum dolor sit amet, consec-<br>tetuer adipiscing elit,</div>

    <div class="connector" style="left:126px;top:346px;width:94px;background:var(--orange)"></div>
    <div class="node" style="left:102px;top:334px;border-color:var(--orange)"></div>
    <div class="step" style="left:220px;top:325px"><b>LOREM IPSUM</b>Lorem ipsum dolor sit amet, consec-<br>tetuer adipiscing elit,</div>

    <div class="connector" style="left:126px;top:443px;width:41px;background:var(--orange)"></div>
    <div class="node" style="left:102px;top:431px;border-color:var(--orange)"></div>
    <div class="step" style="left:167px;top:422px"><b>LOREM IPSUM</b>Lorem ipsum dolor sit amet, consec-<br>tetuer adipiscing elit,</div>

    <div class="connector" style="left:126px;top:540px;width:94px;background:var(--orange)"></div>
    <div class="node" style="left:102px;top:528px;border-color:var(--orange)"></div>
    <div class="step" style="left:220px;top:519px"><b>LOREM IPSUM</b>Lorem ipsum dolor sit amet, consec-<br>tetuer adipiscing elit,</div>

    <div class="connector" style="left:126px;top:637px;width:41px;background:var(--orange)"></div>
    <div class="node" style="left:102px;top:625px;border-color:var(--orange)"></div>
    <div class="step" style="left:167px;top:616px"><b>LOREM IPSUM</b>Lorem ipsum dolor sit amet, consec-<br>tetuer adipiscing elit,</div>

    <div class="connector" style="left:126px;top:735px;width:94px;background:var(--orange)"></div>
    <div class="node" style="left:102px;top:723px;border-color:var(--orange)"></div>
    <div class="step" style="left:220px;top:714px"><b>LOREM IPSUM</b>Lorem ipsum dolor sit amet, consec-<br>tetuer adipiscing elit,</div>

    <svg class="icon" viewBox="0 0 48 48" style="left:30px;top:32px;color:var(--orange)"><path d="M24 6l18 10-18 10L6 16z"/><path d="M6 24l18 10 18-10M6 32l18 10 18-10"/></svg>
    <svg class="icon" viewBox="0 0 48 48" style="left:30px;top:129px;color:var(--orange)"><rect x="7" y="8" width="34" height="32"/><rect x="4" y="5" width="6" height="6"/><rect x="38" y="5" width="6" height="6"/><rect x="4" y="37" width="6" height="6"/><rect x="38" y="37" width="6" height="6"/><path d="M12 24q12-12 24 0q-12 12-24 0z"/><circle cx="24" cy="24" r="4"/></svg>
    <svg class="icon" viewBox="0 0 48 48" style="left:30px;top:226px;color:var(--orange)"><path d="M20 44h24M30 44V32L16 18"/><path d="M8 10l10-6 8 12-14 6z"/><path d="M10 24l-4 6M16 26l-1 7M4 18l-3 1"/></svg>
    <svg class="icon" viewBox="0 0 48 48" style="left:30px;top:323px;color:var(--orange)"><rect x="5" y="7" width="38" height="34" rx="2"/><path d="M5 13h38"/><rect x="11" y="18" width="26" height="18"/></svg>
    <svg class="icon" viewBox="0 0 48 48" style="left:30px;top:420px;color:var(--orange)"><path d="M24 3l19 11v20L24 45 5 34V14z"/><path d="M24 13l10 6v11l-10 6-10-6V19zM14 19l10 6 10-6M24 25v11"/></svg>
    <svg class="icon" viewBox="0 0 48 48" style="left:30px;top:517px;color:var(--orange)"><rect x="4" y="6" width="40" height="24" rx="3"/><path d="M12 14h24M12 20h10"/><circle cx="24" cy="30" r="6"/><path d="M20 35l-2 10 6-4 6 4-2-10"/></svg>
    <svg class="icon" viewBox="0 0 48 48" style="left:30px;top:614px;color:var(--orange)"><circle cx="22" cy="26" r="18"/><circle cx="22" cy="26" r="11"/><circle cx="22" cy="26" r="4"/><path d="M22 26L40 8M34 8h6v6"/></svg>
    <svg class="icon" viewBox="0 0 48 48" style="left:30px;top:712px;color:var(--orange)"><path d="M18 44C8 32 4 24 4 17a14 14 0 0 1 28 0"/><circle cx="18" cy="17" r="5"/><circle cx="33" cy="33" r="11"/><path d="M36 28h-4a2.5 2.5 0 0 0 0 5h2a2.5 2.5 0 0 1 0 5h-4M33 25v16"/></svg>
  </section>

  <!-- Prices -->
  <section class="page prices" style="left:729px;top:901px">
    <div class="abs" style="left:524px;top:-33px;width:124px;height:124px;border-radius:50%;background:var(--yellow)"></div>
    <h2 class="abs heading" style="left:24px;top:20px;color:var(--navy)">Prices and Lorem Ipsum</h2>

    <table class="price-table">
      <tr><th class="row-label" style="background:none"></th><th style="width:96px">1 Bedroom</th><th style="width:104px">2 Bedrooms</th><th style="width:125px">3 Bedrooms</th><th style="width:160px">4 Bedrooms</th></tr>
      <tr class="baths"><td class="row-label">Bathrooms</td><td>1</td><td><div class="spread"><span>1</span><span>2</span></div></td><td><div class="spread"><span>1</span><span>2</span><span>3</span></div></td><td><div class="spread"><span>1</span><span>2</span><span>3</span><span>4</span></div></td></tr>
      <tr class="story"><td class="row-label">1 story</td><td>Values</td><td>Values</td><td>Values</td><td>Values</td></tr>
      <tr class="story"><td class="row-label">2 story</td><td>N/A</td><td>Values</td><td>Values</td><td>Values</td></tr>
    </table>

    <p class="abs body-copy" style="left:23px;top:215px;width:232px;text-align:left">Lorem ipsum dolor sit amet, consectetuer adipiscing elit, sed diam nonummy nibh euismod tincidunt ut laoreet dolore magna aliquam erat volutpat. Ut wisi enim ad minim</p>

    <div class="price-list">
      <div class="price-row"><span class="lbl">Lorem ipsum dolor</span><span class="cur">$</span><span class="amt">100,000.00</span></div>
      <div class="price-row"><span class="lbl">Lorem ipsum dolor</span><span class="cur">$</span><span class="amt">1,000.00</span></div>
      <div class="price-row"><span class="lbl">Lorem ipsum dolor</span><span class="cur">$</span><span class="amt">100.00</span></div>
      <div class="price-row"><span class="lbl">Lorem ipsum dolor</span><span class="cur">$</span><span class="amt">5,000.00</span></div>
      <div class="price-row"><span class="lbl">Lorem ipsum dolor</span><span class="cur">$</span><span class="amt">7,800.00</span></div>
      <div class="price-row" style="margin-top:17px;color:var(--orange)"><span class="lbl">TOTAL</span><span style="width:78px;text-align:right">$ 113,900.00</span></div>
      <div class="price-row"><span>TOTAL SAVE (0.2%)</span></div>
    </div>

    <h2 class="abs heading" style="left:295px;top:230px;color:var(--navy)">Cost Saving</h2>
    <p class="abs body-copy" style="left:296px;top:265px;width:282px"><span class="accent">Lorem ipsum</span> dolor sit amet, consectetuer adipiscing elit, sed diam nonummy nibh euismod tincidunt ut laoreet dolore magna aliquam erat volutpat. Ut wisi enim ad <span class="accent">minim veniam</span>, quis nostrud exerci tation ullamcorper suscipit lobortis nisl ut aliquip ex ea commodo consequat. Duis autem vel eum iriure dolor in hendrerit in vulputate <span class="accent">velit esse</span> molestie consequat, vel illum dolore eu feugiat nulla facilisis at vero eros et accumsan et iusto odio <span class="accent">dignissim</span> qui blandit praesent luptatum zzril delenit augue duis dolore te feugait nulla facilisi.</p>

    <div class="abs" style="left:260px;top:470px;width:357px;height:330px;background:var(--navy)"></div>
    <div class="abs" style="left:0;top:633px;width:617px;height:167px;background:var(--navy)"></div>
    <div class="abs" style="left:278px;top:488px;width:339px;height:145px;background:var(--white)"></div>
    <div class="photo" role="img" aria-label="Photograph of a finished timber-frame home with landscaped garden" style="left:295px;top:446px;width:288px;height:170px;background:linear-gradient(170deg,#8aa27a 0%,#8f6548 45%,#a4583e 62%,#6f8a4e 100%)"></div>

    <div class="abs contact" style="left:282px;top:646px;width:300px">GET ADVICE ON YOUR PROJECT<br>+1 555 010 2040<br><span style="letter-spacing:1.5px;font-size:10.5px">WWW.HARLOWREEDSTUDIO.COM</span></div>
    <div class="abs contact" style="left:253px;top:745px;width:160px;font-size:11px;line-height:14px">MY LOCATION (HQ)<br>41, ELM ROW, NY<br>USA</div>
    <div class="abs contact" style="left:464px;top:745px;width:160px;font-size:11px;line-height:14px">MY LOCATION (1)<br>17, ORCHARD LANE, CA<br>USA</div>
  </section>

  <!-- Additional notes -->
  <section class="page notes" style="left:1391px;top:901px">
    <div class="abs" style="left:0;top:0;width:303px;height:800px;background:var(--navy)"></div>
    <h2 class="abs heading" style="left:327px;top:22px;color:var(--navy)">Lorem Ipsum<br>Additional Notes</h2>
    <div class="abs" style="left:12px;top:777px;color:var(--white);font-size:10.5px;letter-spacing:1.5px">WWW.HARLOWREEDSTUDIO.COM</div>
    <div class="abs brand-name" style="left:303px;top:735px;width:160px;font-size:14px;line-height:16px">Harlow Reed<br>Architect</div>
  </section>

</main>
</body>
</html>
```